Industrial/Commercial Plumbing Capability Statement

Would like a construction capability statement/Brochure amended to be similar to the attached. -
Have included photos and Notes on the attached
would like project photos to be used
This is a previous capability statement that we would like amended and altered to include, safety, QA and Recent Projects
Please use our company logo
Updates

Need extra days to review

Target Market(s)

Construction work - Industrial

Industry/Entity Type

Plumbing

Requirements
Must have
• Include all items in contents page

Eye Catching Photos relevant to construction industry and relevant to topic on page

```html
<!DOCTYPE html>
<html lang="en">
<head>
<meta charset="utf-8">
<title>Northline Plumbers – Capability Statement Spreads</title>
<link href="https://fonts.googleapis.com/css2?family=Barlow:wght@400;500;600;700&family=Nunito:wght@600&display=swap" rel="stylesheet">
<style>
:root{
  --navy:#063a5f;
  --navy-line:#9fb6cc;
  --paper:#ffffff;
  --ink:#0b3a5e;
  --bg:#ffffff;
  --photo-yellow-a:#c9b21a;
  --photo-yellow-b:#8f7a1c;
  --photo-sunset-a:#f2c21b;
  --photo-sunset-b:#d9731a;
  --photo-dark-a:#3a4a12;
  --photo-dark-b:#11160a;
}
*{margin:0;padding:0;box-sizing:border-box}
html,body{width:1200px;height:848px;overflow:hidden;background:var(--bg)}
body{position:relative;font-family:"Barlow",Arial,sans-serif;color:var(--ink)}
.spread{position:absolute;width:488px;height:342px;box-shadow:6px 8px 14px rgba(0,0,0,.22)}
.page{position:absolute;top:0;width:244px;height:342px;overflow:hidden}
.page--left{left:0}.page--right{left:244px}
.navy{background:var(--navy);color:#fff}
.white{background:var(--paper)}
.photo{position:absolute;left:0;top:0;width:244px}
.photo--dig{height:228px;background:linear-gradient(160deg,var(--photo-yellow-a),var(--photo-yellow-b) 70%,#6d5a1a)}
.photo--sunset{height:228px;background:linear-gradient(180deg,var(--photo-sunset-a) 0%,#f0a21b 45%,var(--photo-sunset-b) 65%,#7c6a1e 100%)}
.photo--team{height:174px;background:linear-gradient(140deg,#e6d21a,#c7b817 55%,#8c8a20)}
.photo--keyboard{height:342px;background:radial-gradient(circle at 70% 40%,#5f6f1d 0%,var(--photo-dark-a) 35%,var(--photo-dark-b) 100%)}
.frame{position:absolute;border:0.8px solid var(--navy-line)}
.dot{position:absolute;width:6px;height:6px;border:0.8px solid var(--navy-line);border-radius:50%}
.brand{position:absolute;font-weight:700;font-size:9px;letter-spacing:.3px;color:#fff;display:flex;align-items:center;gap:4px}
.brand i{display:inline-block;width:7px;height:7px;background:#fff}
.cover-title{position:absolute;left:22px;top:232px;font-size:11px;letter-spacing:1.2px;color:#fff;font-weight:400}
.address{position:absolute;left:22px;top:237px;font-size:3.6px;line-height:8px;color:#fff}
.toc{position:absolute;left:53px;top:76px;width:136px}
.toc h2{font-weight:400;font-size:13.5px;color:var(--ink);letter-spacing:.2px;margin:0 0 2px 5px}
.toc ul{list-style:none;margin-left:5px}
.toc li{display:flex;font-size:6.8px;line-height:12.2px;color:var(--ink);text-transform:uppercase;white-space:nowrap}
.toc li .leader{flex:1;border-bottom:0.7px dotted var(--ink);margin:0 1px 3.5px}
.label{position:absolute;font-size:3.8px;font-weight:700;text-transform:uppercase;line-height:4.4px;color:#fff}
.heading{position:absolute;font-weight:400;font-size:13.5px;color:#fff;letter-spacing:.2px;white-space:nowrap}
.body{position:absolute;font-size:3.4px;line-height:5.7px;color:#fff}
.body p{margin-bottom:2.6px}
.quote{position:absolute;font-family:"Nunito",Arial,sans-serif;font-weight:600;font-size:4.9px;line-height:9.3px}
.quote--navy{left:120px;top:254px;width:74px;color:#fff}
.quote--white{left:54px;top:186px;width:132px;color:var(--ink)}
.quote--caption{left:126px;top:253px;width:54px;color:#fff;text-align:center}
.globe{position:absolute;left:20px;top:77px;width:116px;height:116px;border-radius:50%;border:1px solid #d8e21f;background:radial-gradient(circle,rgba(40,90,80,.85) 35%,rgba(200,210,30,.25) 70%,rgba(200,210,30,.1))}
.globe-text{position:absolute;left:52px;top:112px;width:52px;text-align:center;font-size:6.6px;line-height:9.4px;color:#fff}
.folio{position:absolute;bottom:20px;font-size:2.3px;font-weight:700;text-transform:uppercase;display:flex;align-items:center;gap:2px;white-space:nowrap}
.folio b{display:inline-block;width:5px;height:5px;border-radius:50%;background:var(--navy);color:#fff;font-size:2.4px;text-align:center;line-height:5px}
.folio--light{color:#fff}.folio--light b{background:#fff;color:var(--navy)}
.folio--dark{color:var(--ink)}
.folio-stem{position:absolute;bottom:0;width:0.8px;height:12px;background:var(--navy-line)}
.member{position:absolute;left:18px;width:214px;display:flex;gap:9px}
.member .portrait{flex:none;width:55px;height:42px;background:linear-gradient(180deg,#d8d8d8,#9a9a9a)}
.member .bio{width:146px}
.member h3{font-size:7px;font-weight:400;color:#fff;line-height:8px;text-transform:uppercase;white-space:nowrap}
.member h3 strong{font-weight:700}
.member p{font-size:3.1px;line-height:5.6px;color:#fff;margin-top:1px}
</style>
</head>
<body>

<section class="spread" style="left:90px;top:61px">
  <div class="page page--left navy">
    <div class="photo photo--dig" role="img" aria-label="Excavator and site worker beside a pipe trench, yellow toned photograph"></div>
    <div class="frame" style="left:0;top:228px;width:172px;height:20px;border-top:none;border-left:none;border-radius:0 0 4px 0"></div>
    <div class="dot" style="left:169px;top:222px"></div>
    <div class="cover-title">CAPABILITY STATEMENT</div>
    <div class="brand" style="left:22px;top:311px"><i></i>NORTHLINE PLUMBERS.</div>
  </div>
  <div class="page page--right navy">
    <div class="photo photo--sunset" role="img" aria-label="City skyline across a river at sunset, orange toned photograph"></div>
    <div class="frame" style="left:0;top:228px;width:173px;height:42px;border-top:none;border-left:none;border-radius:0 0 4px 0"></div>
    <div class="dot" style="left:170px;top:222px"></div>
    <div class="address">42 Harbour Lane Westfield WA 6100<br>PO Box 2281 Westfield DC WA 6901<br>(08) 9000 1234<br>northlineplumbers.com.au</div>
    <div class="brand" style="left:22px;top:311px"><i></i>NORTHLINE PLUMBERS.</div>
  </div>
</section>

<section class="spread" style="left:622px;top:61px">
  <div class="page page--left navy"></div>
  <div class="page page--right white">
    <div class="frame" style="left:47px;top:69px;width:197px;height:24px;border-right:none;border-bottom:none;border-radius:4px 0 0 0"></div>
    <div class="dot" style="left:44px;top:91px"></div>
    <nav class="toc">
      <h2>TABLE OF CONTENTS</h2>
      <ul>
        <li>From the directors<span class="leader"></span>3</li>
        <li>About the business<span class="leader"></span>4</li>
        <li>Our services<span class="leader"></span>6</li>
        <li>Safety<span class="leader"></span>8</li>
        <li>Quality assurance<span class="leader"></span>10</li>
        <li>Recent projects<span class="leader"></span>12</li>
        <li>Meet the team<span class="leader"></span>14</li>
      </ul>
    </nav>
    <div class="folio folio--dark" style="left:100px">Northline Plumbers <b>02</b> Capability Statement</div>
    <div class="folio-stem" style="left:121px"></div>
  </div>
</section>

<section class="spread" style="left:90px;top:445px">
  <div class="page page--left navy">
    <div class="frame" style="left:0;top:9px;width:63px;height:14px;border-left:none;border-bottom:none;border-radius:0 4px 0 0"></div>
    <div class="dot" style="left:60px;top:22px"></div>
    <div class="label" style="left:19px;top:16px">The company</div>
    <h1 class="heading" style="left:55px;top:40px">ABOUT THE BUSINESS</h1>
    <div class="body" style="left:48px;top:62px;width:147px">
      <p>Established in 2004 by its two managing directors, Northline Plumbers specialises in the commercial sector and has extensive expertise in all levels of the industry, from new shopping centres, hotels and high rise developments to hospitals and industrial equipment in both construction and maintenance.</p>
      <p>Our relationships with our suppliers are central to the success of our business, and we hold trading accounts with all major plumbing suppliers in the region. We maintain close working relationships with manufacturers to ensure</p>
      <p>that we are at the forefront of advancements within the plumbing industry, both in products and in plumbing techniques.</p>
      <p>We strive for a balance in cost effective plumbing while keeping the highest standards in the industry. We are relentless in our pursuit of quality and excellence in service. Our approach is built on collaboration, innovation, integrity and accountability, which underpin every interaction at each stage of the work we do. We focus on the relationships we build with our customers, colleagues and stakeholders to ensure the best outcomes.</p>
      <p>At Northline Plumbers we believe our excellent customer relations, passion for the industry and our expertise mean we can deliver what we promise. We know this sets us apart, as our satisfied customers keep coming back and recommend us to others.</p>
      <p>We know that our success, and the success of our projects, depends on the quality of our people. We are committed to attracting and retaining talented employees by providing a strong platform for ongoing career development.</p>
      <p>We proudly employ a highly skilled team of full time staff ranging from qualified trades people and apprentices to administration personnel. We are committed to the regular ongoing training and cross skilling of all our staff and promote a workplace culture that supports career advancement as well as professional and personal growth.</p>
    </div>
    <div class="frame" style="left:0;top:247px;width:202px;height:24px;border-left:none;border-bottom:none;border-radius:0 4px 0 0"></div>
    <div class="dot" style="left:199px;top:270px"></div>
    <div class="quote quote--navy">“Northline Plumbers having extensive expertise across many areas, from new Shopping centres and Hospitals to industrial equipment.”</div>
    <div class="folio folio--light" style="left:102px">Northline Plumbers <b>03</b> Capability Statement</div>
    <div class="folio-stem" style="left:122px"></div>
  </div>
  <div class="page page--right white">
    <div class="photo photo--team" role="img" aria-label="Two site managers in hard hats reviewing plans, yellow toned photograph"></div>
    <div class="frame" style="left:47px;top:180px;width:197px;height:24px;border-right:none;border-bottom:none;border-radius:4px 0 0 0"></div>
    <div class="dot" style="left:44px;top:202px"></div>
    <div class="quote quote--white">“As commercial Builders we often have to work on difficult Projects that require unique, innovative results. Northline Plumbers are problem solvers and work closely with our team to deliver high quality solution oriented Projects. We started working with Northline Plumbers several years ago and continue to be impressed by their professionalism and attention to detail.”</div>
    <div class="folio folio--dark" style="left:100px">Northline Plumbers <b>04</b> Capability Statement</div>
    <div class="folio-stem" style="left:121px"></div>
  </div>
</section>

<section class="spread" style="left:622px;top:445px">
  <div class="page page--left">
    <div class="photo photo--keyboard" role="img" aria-label="Hand typing on a keyboard with a glowing network graphic, dark green and yellow toned photograph"></div>
    <div class="frame" style="left:0;top:9px;width:63px;height:14px;border-left:none;border-bottom:none;border-radius:0 4px 0 0"></div>
    <div class="label" style="left:19px;top:16px">Online asset<br>management</div>
    <div class="globe"></div>
    <div class="globe-text">Manage your plumbing services at the push of a button.</div>
    <div class="frame" style="left:0;top:247px;width:182px;height:24px;border-left:none;border-bottom:none;border-radius:0 4px 0 0"></div>
    <div class="dot" style="left:179px;top:270px"></div>
    <div class="quote quote--caption">An online asset management system designed for commercial property management.</div>
    <div class="folio folio--light" style="left:100px">Northline Plumbers <b>05</b> Capability Statement</div>
    <div class="folio-stem" style="left:121px"></div>
  </div>
  <div class="page page--right navy">
    <div class="frame" style="left:181px;top:9px;width:63px;height:14px;border-right:none;border-bottom:none;border-radius:4px 0 0 0"></div>
    <div class="label" style="left:187px;top:16px">Meet the team</div>
    <article class="member" style="top:42px">
      <div class="portrait" role="img" aria-label="Portrait photo of the managing director"></div>
      <div class="bio"><h3><strong>Daniel Reeves</strong> Managing Director</h3><p>Daniel believes that quality professional relationships are built on the four key values of respect, integrity, teamwork and accountability. His aim is to provide business focused solutions to the companies he works with, and gain a thorough understanding of each organisation in order to work as a partner rather than a contractor. A licensed plumber and registered builder with over twenty years of experience in commercial construction and maintenance, he takes a hands on approach, working closely with clients, consultants and authorities to deliver each project from concept to completion.</p></div>
    </article>
    <article class="member" style="top:108px">
      <div class="portrait" role="img" aria-label="Portrait photo of the second managing director"></div>
      <div class="bio"><h3><strong>Marco Bellini</strong> Managing Director</h3><p>Marco is passionate about providing quality service of the highest possible standard and leads the way in adopting new industry methods. Through collaboration with his fellow director and a commitment to understanding each client's needs, his professional approach keeps the whole team on track. Marco has over twenty years of experience in large scale commercial plumbing. As a licensed plumber and registered builder he is an expert in all aspects of building and construction, and enjoys working on site.</p></div>
    </article>
    <article class="member" style="top:175px">
      <div class="portrait" role="img" aria-label="Portrait photo of the construction manager"></div>
      <div class="bio"><h3><strong>Sam Whitford</strong> Construction Manager</h3><p>Sam has been involved in large scale commercial and construction plumbing for over ten years, working in a variety of settings across the country. He has been an integral part of the Northline Plumbers team since 2012, overseeing all construction projects. His strong work ethic means he is highly respected on site and ensures that every project runs efficiently and is completed on time to all specifications.</p></div>
    </article>
    <article class="member" style="top:242px">
      <div class="portrait" role="img" aria-label="Portrait photo of the operations manager"></div>
      <div class="bio"><h3><strong>Chris Langley</strong> Operations Manager</h3><p>Chris has over fifteen years of project management experience in the commercial plumbing and construction industry. His impressive work history on large scale infrastructure means he has a high level of technical knowledge, combined with an in depth understanding of business management. His focus is on building quality relationships and maintaining effective communication with all stakeholders so clients have a positive experience at every stage of the project.</p></div>
    </article>
    <div class="folio folio--light" style="left:100px">Northline Plumbers <b>06</b> Capability Statement</div>
    <div class="folio-stem" style="left:121px"></div>
  </div>
</section>

</body>
</html>
```